MODERN + COOL Business Card Needed!

SUMMARY
This is for a 40+ year old family business that is transitioning to the 2nd generation and is in real need of a more modern facelift. Ive attached a company logo (I made quickly as an idea with my limited PSD skills) to start off with that you are welcome to change and draw ideas from. Ive also attached some screen shots of cards I like to give you an idea of my preferences.

WHAT WE DO
The company name is Tall Pine HK Ltd. But I prefer to just call it Tall Pine or Tall Pine with Hong Kong as kind of a sub heading on the business card. We own a factory as well as help our customers find factories to make their product. Product I mean, toys 99.9% of the time. Simple old school toys like board games, puzzles, wooden toys, baby/infant toys.

You can say we are a "sourcing" or "trading" or "consulting" company with a factory to help you do it. But since we deal with toys, i like to keep it modern and cool and fun, not serious like managing hedge funds.

WHAT WE ARE LOOKING FOR
A cool, unique looking business card that stands out. In terms of design, something modern and professional. I like darker colored cards and I like colors such as blue/green/dark gray, but am open to other colored themes. I Like bright lime green with gray, always though thats a nice combo. I prefer cards that are all colored and not so much white showing (I think). Ive attached a few screenshots of cards so take a look to get a feel of what I like.

We do alot of wooden stacking games in variety of colors too like Tovra, Lumo, Towerplix (google these to check them out). So designs that sort of resemble stacking or building would be cool but totally not necessary.

In terms of the physical aspects of the card, Im looking for a card a bit different than the standard rectangular shape. Double sided. Little things like having corner(s) be round or different angle instead of square edge I always thought was nice. Its got to be mostly a normal card size, no folding or smaller cards that fit weird in your wallet. No vertical designs. Am open to VERY different/creative shapes (as long as it still fits in a wallet good like a normal buisness card.
Updates

Hi everyone!

Just wanted to write a message to everyone to let them know all submissions are being reviewed or have been reviewed.  If I have not responded with feedback, rest assure your submission was definitely looked at in detail but I either have just been too busy to respond (alot of submissions!), or its on my to be considered list.

I respect and really enjoy receiving everyones creativity and work so I dont want it to go unrecognized - thus this message!  Feel free to submit more ideas if you like until this project ends.  Sometimes some designs just dont click but sometimes they can so you never know!

Thanks again for everyones participation and great work!

~Dev Orr

Target Market(s)

The cards are mainly handed to toy company sourcers and buyers. People I talk to ... say Pelvane for example... might want to make their next edition of Farthingale game with a reputable factory at a good cost so they can sell it to stores at a profit.

So these are the types of people I often try to talk and introduce myself and my company to.

Industry/Entity Type

Building

Colors
acd036
0392cd
00a88e
474747
606060

Requirements
Must have
• Just double sided, not plain rectangle corners, and just cool to look at and catches your eye!

Oh and the obvious business card stuff like place for name, address, number, email, etc.
Nice to have
• Think more modern and fun, not serious and old fashion (thats what we used to be!). Can use the logo I attached and you can definitely alter and change the logo or make a whole new one!

Oh and can definitely use a creative slogan if you like to think of one based on what I described in what we do.
Should not have
• Dont use fonts or text placement that might make "Tall Pine" look like "Tal Lpine"... We arent selling news papers!!

Please nothing related to education since we have the word Pine in the title, thats not our business at all.

Logo and design should not be too heavy on things related to toys, as though thats what we primarily focus on now, what we do may change over time.

```html
<!DOCTYPE html>
<html lang="en">
<head>
<meta charset="utf-8">
<title>Tall Pine Ltd — Business Card</title>
<link rel="stylesheet" href="https://fonts.googleapis.com/css2?family=Tinos:wght@400;700&family=PT+Sans&display=swap">
<style>
  :root {
    --lime: #acd036;
    --charcoal: #474747;
    --ink: #3a3a3a;
    --paper: #ffffff;
    --frame: #222222;
    --label: #111111;
  }
  * { margin: 0; padding: 0; box-sizing: border-box; }
  html, body { width: 1200px; height: 1200px; overflow: hidden; background: var(--paper); }
  .sheet {
    position: relative;
    width: 1200px;
    height: 1200px;
    border: 1px solid var(--frame);
    background: var(--paper);
    font-family: "Tinos", "Times New Roman", serif;
  }
  .side-label {
    position: absolute;
    left: 54px;
    font-family: "PT Sans", "Myriad Pro", sans-serif;
    font-size: 31px;
    color: var(--label);
    line-height: 1;
  }
  .side-label--front { top: 268px; }
  .side-label--back { top: 897px; }

  .card {
    position: absolute;
    left: 182px;
    width: 833px;
    overflow: hidden;
    display: flex;
    flex-direction: column;
    gap: 2px;
    background: var(--paper);
  }
  .card--front {
    top: 70px;
    height: 483px;
    border-top-left-radius: 175px;
    border-bottom-right-radius: 175px;
  }
  .card--back {
    top: 643px;
    height: 484px;
    border-top-right-radius: 175px;
    border-bottom-left-radius: 175px;
    gap: 3px;
  }
  .band { position: relative; width: 100%; }
  .band--lime { background: var(--lime); }
  .band--charcoal { background: var(--charcoal); }
  .card--front .band--lime { height: 251px; }
  .card--front .band--charcoal { flex: 1; }
  .card--back .band--charcoal { height: 250px; }
  .card--back .band--lime { flex: 1; }

  .brand-mark {
    position: absolute;
    left: 0; right: 0;
    top: 100px;
    text-align: center;
    color: var(--paper);
    font-weight: 700;
    font-size: 60px;
    line-height: 1;
    letter-spacing: -1px;
  }
  .company {
    position: absolute;
    left: 0; right: 0;
    top: 76px;
    text-align: center;
    color: var(--paper);
    font-weight: 700;
    line-height: 1;
  }
  .company__name { font-size: 54px; letter-spacing: -1px; }
  .company__city { font-size: 32px; margin-top: -3px; letter-spacing: -0.5px; }

  .person {
    position: absolute;
    left: 0; right: 0;
    top: 109px;
    text-align: center;
    color: var(--paper);
    line-height: 1;
  }
  .person__name { font-size: 29px; }
  .person__title { font-size: 13px; margin-top: 2px; }

  .contact {
    position: absolute;
    left: 0; right: 0;
    top: 158px;
    text-align: center;
    color: var(--ink);
    font-size: 13px;
    line-height: 25px;
  }
</style>
</head>
<body>
  <main class="sheet">
    <span class="side-label side-label--front">Front</span>
    <section class="card card--front" aria-label="Card front">
      <div class="band band--lime">
        <div class="brand-mark">tall pine</div>
      </div>
      <div class="band band--charcoal">
        <div class="company">
          <div class="company__name">tall pine ltd</div>
          <div class="company__city">hong kong</div>
        </div>
      </div>
    </section>

    <span class="side-label side-label--back">Back</span>
    <section class="card card--back" aria-label="Card back">
      <div class="band band--charcoal">
        <div class="person">
          <div class="person__name">Dev Orr</div>
          <div class="person__title">Managing Director</div>
        </div>
      </div>
      <div class="band band--lime">
        <div class="contact">
          <div class="contact__email">Email: devorr@tallpineltd.com</div>
          <div class="contact__web">www.tallpineltd.com</div>
        </div>
      </div>
    </section>
  </main>
</body>
</html>
```